Banner Ad Design Project

I need a banner design. The website is under construction at www.brightmarrow.example

Name: Bright Marrow
Tagline: Steady Sparks for crowded calendars

This is a leadership development and executive coaching site. The past site is live at www.quillstepnow.example. (so you can get a sense of the content)

The audience are (BUSY) executives, senior managers, leaders and top professionals, so the feel needs to be highly professional but also modern and fresh. I want to communicate energy but also solid and trust worthy and not too new agey. The audience are also people with strong social values who want to change things - so not too corporate (Ie suits!)

I would like the design to be floating on a white background, very clean and simple. I am attracted to reds or sunset (burn orange crimson colors.) But totally open to any color ideas.
I am giving an open brief for your ideas.
Here are the dimensions 960px wide, roughly 190px height.

Reason: The weekend might give more time to designers to get involved. Thanks Vina

Hi designers

You may not have seen the additions I gave to this brief.

The banner should not have leader out front photo's. Maybe less corporate than I initially thought. 
Not too corporate (no suits!) Please no chess pieces, jigsaw pieces, cartoon images, cliche leadership images. 
Am am trying for inspiration /inspiring whilst still being professional. Very simple and clean.
Please can the design be floating in a white background so that the web page is borderless - A bit like it is in http://palmoriskel.example/
Thank you

Target Market(s)

Senior managers, executives but people who also want to change the world!

Industry/Entity Type

Construction

Requirements
Should not have
• Should not have leader out front photo's.
Maybe less corporate than I initially thought.
Am am trying for inspiration /inspiring whilst still being professional.
Please no chess pieces, jigsaw pieces, cartoon images, cliche leadership images. Not too corporate (Ie suits!)

Thanks

```html
<!DOCTYPE html>
<html lang="en">
<head>
<meta charset="utf-8">
<title>Bright Marrow banner</title>
<link rel="stylesheet" href="https://fonts.googleapis.com/css2?family=Archivo+Black&family=Arimo:wght@400&display=swap">
<style>
  :root {
    --page: #ffffff;
    --brand-orange: #f7931e;
    --tagline-green: #2f9e2f;
    --play-red: #e0251b;
    --play-ring: #c9c9c9;
    --sky-top: #5f8fc4;
    --sky-mid: #a9c6e4;
    --snow: #f3f6f9;
    --photo-edge: #ffffff;
  }
  html, body {
    margin: 0;
    padding: 0;
    width: 1200px;
    height: 238px;
    overflow: hidden;
    background: var(--page);
  }
  .banner {
    position: relative;
    width: 1200px;
    height: 238px;
    background: var(--page);
  }
  .brand-name {
    position: absolute;
    left: 108px;
    top: 44px;
    width: 520px;
    height: 100px;
  }
  .brand-name text {
    font-family: "Archivo Black", "Arial Black", sans-serif;
    font-size: 78px;
    fill: var(--brand-orange);
  }
  .tagline {
    position: absolute;
    left: 112px;
    top: 150px;
    display: flex;
    align-items: center;
    gap: 14px;
  }
  .tagline-icon {
    width: 30px;
    height: 30px;
    flex: none;
  }
  .tagline-text {
    font-family: "Arimo", Arial, sans-serif;
    font-size: 24px;
    color: var(--tagline-green);
    letter-spacing: 0.2px;
    white-space: nowrap;
  }
  .hero-photo {
    position: absolute;
    left: 718px;
    top: 8px;
    width: 432px;
    height: 222px;
  }
</style>
</head>
<body>
  <div class="banner">
    <svg class="brand-name" viewBox="0 0 520 100" aria-label="Bright Marrow">
      <text x="4" y="76" textLength="508" lengthAdjust="spacingAndGlyphs">Bright Marrow</text>
    </svg>

    <div class="tagline">
      <svg class="tagline-icon" viewBox="0 0 30 30" aria-hidden="true">
        <circle cx="15" cy="15" r="13.5" fill="#ffffff" stroke="var(--play-ring)" stroke-width="2"/>
        <path d="M11.5 9.5 L20.5 15 L11.5 20.5 Z" fill="var(--play-red)"/>
      </svg>
      <span class="tagline-text">Steady Sparks for crowded calendars</span>
    </div>

    <svg class="hero-photo" viewBox="0 0 432 222" role="img" aria-label="Photo: a few penguins standing on open snow under a blue sky, one walking ahead">
      <defs>
        <linearGradient id="sky-to-snow" x1="0" y1="0" x2="0" y2="1">
          <stop offset="0" stop-color="var(--sky-top)"/>
          <stop offset="0.5" stop-color="var(--sky-mid)"/>
          <stop offset="0.72" stop-color="var(--snow)"/>
          <stop offset="1" stop-color="#e6ecf2"/>
        </linearGradient>
        <filter id="soft-shadow" x="-5%" y="-5%" width="110%" height="115%">
          <feDropShadow dx="1" dy="2" stdDeviation="2" flood-color="#000" flood-opacity="0.25"/>
        </filter>
      </defs>
      <path filter="url(#soft-shadow)" fill="url(#sky-to-snow)" stroke="var(--photo-edge)" stroke-width="1.5"
        d="M6 6 L60 4 L120 7 L190 3 L260 6 L330 4 L400 6 L426 5 L428 40 L425 90 L428 140 L425 190 L427 216
           L360 218 L290 215 L220 219 L150 216 L80 219 L8 217 L5 170 L8 120 L4 70 L7 30 Z"/>
    </svg>
  </div>
</body>
</html>
```